Banner to celebrate Pellway Journeys 40 years in business. Will be used on our social media channels.

Hello
We would like a banner created to celebrate 40 years in business with tagline "service through experience since 1983"
also add our website pellwayjourneys.com.au
Banner size must be : 650 x 150px
open to suggestions

Target Market(s)

current and prospective clients

Industry/Entity Type

Travel & Tourism (Business Travel)

Colors
0054AA
0677BA
7BADD7
CADEEF
E8F1F8

Requirements
Must have
• use current theme of our website www.pellwayjourneys.com.au. Keep simple and effective.
Nice to have
• use one image that I have provided
Should not have
• multiple graphics

```html
<!DOCTYPE html>
<html lang="en">
<head>
<meta charset="utf-8">
<title>Pellway Journeys – 40 Years Banner Set</title>
<link rel="stylesheet" href="https://fonts.googleapis.com/css2?family=Oswald:wght@400;500;600;700&family=Poppins:wght@400;500;600;700&display=swap">
<style>
  :root {
    --board-top: #1a5e99;
    --board-bottom: #2a77b5;
    --header-band: #175890;
    --navy: #0b1d47;
    --brand-blue: #1f80d8;
    --accent-red: #e9472a;
    --gold: #f1c232;
    --gold-soft: #f5e6b8;
    --white: #ffffff;
    --label: #eaf2fa;
  }
  * { box-sizing: border-box; margin: 0; padding: 0; }
  html, body { width: 1200px; height: 720px; overflow: hidden; }
  body {
    position: relative;
    background: linear-gradient(160deg, var(--board-top), var(--board-bottom) 55%, var(--board-top));
    font-family: "Poppins", sans-serif;
  }
  .board-header {
    position: absolute; left: 0; top: 0; width: 1200px; height: 64px;
    background: var(--header-band);
  }
  .section-title {
    position: absolute; top: 17px;
    font-family: "Poppins", sans-serif; font-weight: 700;
    font-size: 25px; letter-spacing: 1px; color: var(--white);
    transform: translateX(-50%);
  }
  .section-title--horizontal { left: 308px; }
  .section-title--vertical { left: 916px; }
  .banner-label {
    position: absolute; transform: translateX(-50%);
    font-family: "Poppins", sans-serif; font-weight: 400;
    font-size: 17px; color: var(--label); letter-spacing: .5px;
    white-space: nowrap;
  }
  .banner {
    position: absolute; display: block;
    box-shadow: 0 6px 18px rgba(5, 30, 70, .25);
  }
  .fill-white { fill: var(--white); }
  .fill-navy { fill: var(--navy); }
  .fill-blue { fill: var(--brand-blue); }
  .fill-red { fill: var(--accent-red); }
  .fill-gold { fill: var(--gold); }
  .fill-gold-soft { fill: var(--gold-soft); opacity: .55; }
  .stroke-blue { stroke: var(--brand-blue); fill: none; stroke-width: 1.6; stroke-linecap: round; stroke-linejoin: round; }
  .stroke-navy { stroke: var(--navy); fill: none; stroke-width: 1; }
  .brand-name { font-family: "Poppins", sans-serif; font-weight: 700; fill: var(--navy); }
  .headline { font-family: "Oswald", sans-serif; font-weight: 600; fill: var(--white); }
  .big-number { font-family: "Oswald", sans-serif; font-weight: 700; fill: var(--white); }
  .tag-text { font-family: "Oswald", sans-serif; font-weight: 600; fill: var(--white); }
  .tagline { font-family: "Oswald", sans-serif; font-weight: 500; fill: var(--white); }
  .tagline--light { font-weight: 400; }
  .tagline-year { fill: var(--brand-blue); }
  .visit-text { font-family: "Oswald", sans-serif; font-weight: 600; fill: var(--white); }
  .web-address { font-family: "Poppins", sans-serif; font-weight: 600; fill: var(--navy); }
  .web-address--condensed { font-family: "Oswald", sans-serif; font-weight: 500; }
</style>
</head>
<body>
  <header class="board-header">
    <h1 class="section-title section-title--horizontal">HORIZONTAL</h1>
    <h1 class="section-title section-title--vertical">VERTICAL</h1>
  </header>

  <p class="banner-label" style="left:311px; top:92px;">BANNER-1 (650X150)</p>
  <p class="banner-label" style="left:311px; top:300px;">BANNER-2 (650X150)</p>
  <p class="banner-label" style="left:311px; top:508px;">BANNER-3 (650X150)</p>
  <p class="banner-label" style="left:914px; top:92px;">BANNER-(650X150)</p>

  <!-- Horizontal banner 1 -->
  <svg class="banner banner--wide" style="left:57px; top:134px;" width="520" height="120" viewBox="0 0 650 150">
    <defs>
      <clipPath id="clip-wide-1"><rect width="650" height="150"/></clipPath>
      <linearGradient id="photo-wide-1" x1="0" x2="1" y1="0" y2="1">
        <stop offset="0" stop-color="#e6e2da"/><stop offset=".5" stop-color="#a08868"/><stop offset="1" stop-color="#5d4a3a"/>
      </linearGradient>
    </defs>
    <g clip-path="url(#clip-wide-1)">
      <rect class="fill-white" width="650" height="150"/>
      <g class="confetti">
        <ellipse class="fill-gold-soft" cx="40" cy="20" rx="26" ry="14"/>
        <ellipse class="fill-gold-soft" cx="230" cy="95" rx="26" ry="22"/>
        <ellipse class="fill-gold-soft" cx="150" cy="60" rx="30" ry="16"/>
        <rect class="fill-gold" x="182" y="28" width="8" height="8" transform="rotate(40 186 32)"/>
        <rect class="fill-gold" x="400" y="6" width="5" height="10" transform="rotate(20 402 11)"/>
        <rect class="fill-gold" x="470" y="4" width="4" height="10" transform="rotate(30 472 9)"/>
      </g>
      <g role="img" aria-label="Photo: business traveller walking through an airport terminal with a suitcase">
        <rect x="470" width="180" height="150" fill="url(#photo-wide-1)"/>
      </g>
      <circle class="fill-blue" cx="393" cy="95" r="150"/>
      <circle class="fill-navy" cx="383" cy="95" r="140"/>
      <text class="brand-name" x="14" y="38" font-size="15.5">Pellway Journeys</text>
      <text class="headline" x="384" y="39" font-size="17" text-anchor="middle">CELEBRATE</text>
      <text class="big-number" x="373" y="118" font-size="88" text-anchor="middle">40</text>
      <g transform="translate(408 78) rotate(12)">
        <polygon class="fill-red" points="-26,-11 28,-11 23,0 28,11 -26,11"/>
        <text class="tag-text" x="0" y="5" font-size="14" text-anchor="middle" transform="skewX(-12)">YEARS</text>
      </g>
      <text class="tagline" x="386" y="137" font-size="13.5" text-anchor="middle">SERVICE THROUGH EXPERIENCE SINCE 1983</text>
      <rect class="fill-blue" x="6" y="90" width="60" height="22" rx="11"/>
      <text class="visit-text" x="36" y="106.5" font-size="14" text-anchor="middle">VISIT</text>
      <path class="stroke-blue" d="M72 98 q3 11 16 13 M83 106 l5 5 -6 3"/>
      <g transform="translate(14 129)">
        <circle class="stroke-navy" r="5"/><ellipse class="stroke-navy" rx="2.2" ry="5"/><line class="stroke-navy" x1="-5" x2="5"/>
      </g>
      <text class="web-address" x="23" y="133" font-size="10.5">www.pellwayjourneys.com.au</text>
    </g>
  </svg>

  <!-- Horizontal banner 2 -->
  <svg class="banner banner--wide" style="left:52px; top:340px;" width="520" height="120" viewBox="0 0 650 150">
    <defs>
      <clipPath id="clip-wide-2"><rect width="650" height="150"/></clipPath>
      <linearGradient id="photo-wide-2" x1="0" x2="1" y1="0" y2="1">
        <stop offset="0" stop-color="#dde6e8"/><stop offset=".55" stop-color="#8fa3a2"/><stop offset="1" stop-color="#4e5a5a"/>
      </linearGradient>
    </defs>
    <g clip-path="url(#clip-wide-2)">
      <rect class="fill-white" width="650" height="150"/>
      <g class="confetti">
        <ellipse class="fill-gold-soft" cx="40" cy="20" rx="26" ry="14"/>
        <ellipse class="fill-gold-soft" cx="230" cy="95" rx="26" ry="22"/>
        <ellipse class="fill-gold-soft" cx="150" cy="60" rx="30" ry="16"/>
        <rect class="fill-gold" x="182" y="28" width="8" height="8" transform="rotate(40 186 32)"/>
        <rect class="fill-gold" x="398" y="4" width="5" height="10" transform="rotate(20 400 9)"/>
        <rect class="fill-gold" x="470" y="4" width="4" height="10" transform="rotate(30 472 9)"/>
      </g>
      <g role="img" aria-label="Photo: smiling woman in a grey coat checking her phone in an airport with a handbag">
        <rect x="470" width="180" height="150" fill="url(#photo-wide-2)"/>
      </g>
      <circle class="fill-blue" cx="393" cy="95" r="150"/>
      <circle class="fill-navy" cx="383" cy="95" r="140"/>
      <text class="brand-name" x="14" y="38" font-size="15.5">Pellway Journeys</text>
      <text class="headline" x="384" y="39" font-size="17" text-anchor="middle">CELEBRATE</text>
      <text class="big-number" x="373" y="118" font-size="88" text-anchor="middle">40</text>
      <g transform="translate(408 78) rotate(12)">
        <polygon class="fill-red" points="-26,-11 28,-11 23,0 28,11 -26,11"/>
        <text class="tag-text" x="0" y="5" font-size="14" text-anchor="middle" transform="skewX(-12)">YEARS</text>
      </g>
      <text class="tagline tagline--light" x="384" y="137" font-size="13.5" text-anchor="middle">SERVICE THROUGH EXPERIENCE SINCE <tspan class="tagline-year">1983</tspan></text>
      <rect class="fill-blue" x="6" y="90" width="60" height="22" rx="11"/>
      <text class="visit-text" x="36" y="106.5" font-size="14" text-anchor="middle">VISIT</text>
      <path class="stroke-blue" d="M72 98 q3 11 16 13 M83 106 l5 5 -6 3"/>
      <g transform="translate(14 129)">
        <circle class="stroke-navy" r="5"/><ellipse class="stroke-navy" rx="2.2" ry="5"/><line class="stroke-navy" x1="-5" x2="5"/>
      </g>
      <text class="web-address" x="23" y="133" font-size="10.5">www.pellwayjourneys.com.au</text>
    </g>
  </svg>

  <!-- Horizontal banner 3 -->
  <svg class="banner banner--wide" style="left:52px; top:555px;" width="520" height="120" viewBox="0 0 650 150">
    <defs>
      <clipPath id="clip-wide-3"><rect width="650" height="150"/></clipPath>
      <linearGradient id="photo-wide-3" x1="0" x2="1" y1="0" y2="1">
        <stop offset="0" stop-color="#f2f3f5"/><stop offset=".5" stop-color="#c9b79c"/><stop offset="1" stop-color="#6f8aa6"/>
      </linearGradient>
    </defs>
    <g clip-path="url(#clip-wide-3)">
      <rect class="fill-white" width="650" height="150"/>
      <g class="confetti">
        <ellipse class="fill-gold-soft" cx="40" cy="20" rx="26" ry="14"/>
        <ellipse class="fill-gold-soft" cx="230" cy="95" rx="26" ry="22"/>
        <ellipse class="fill-gold-soft" cx="150" cy="60" rx="30" ry="16"/>
        <rect class="fill-gold" x="182" y="28" width="8" height="8" transform="rotate(40 186 32)"/>
        <rect class="fill-gold" x="398" y="4" width="5" height="10" transform="rotate(20 400 9)"/>
        <rect class="fill-gold" x="470" y="4" width="4" height="10" transform="rotate(30 472 9)"/>
      </g>
      <g role="img" aria-label="Photo: cheerful colleagues working together at a laptop in a bright office">
        <rect x="470" width="180" height="150" fill="url(#photo-wide-3)"/>
      </g>
      <circle class="fill-blue" cx="393" cy="95" r="150"/>
      <circle class="fill-navy" cx="383" cy="95" r="140"/>
      <text class="brand-name" x="14" y="38" font-size="15.5">Pellway Journeys</text>
      <text class="headline" x="384" y="39" font-size="17" text-anchor="middle">CELEBRATE</text>
      <text class="big-number" x="373" y="118" font-size="88" text-anchor="middle">40</text>
      <g transform="translate(408 78) rotate(12)">
        <polygon class="fill-red" points="-26,-11 28,-11 23,0 28,11 -26,11"/>
        <text class="tag-text" x="0" y="5" font-size="14" text-anchor="middle" transform="skewX(-12)">YEARS</text>
      </g>
      <text class="tagline tagline--light" x="384" y="137" font-size="13.5" text-anchor="middle">SERVICE THROUGH EXPERIENCE SINCE <tspan class="tagline-year">1983</tspan></text>
      <rect class="fill-blue" x="6" y="90" width="60" height="22" rx="11"/>
      <text class="visit-text" x="36" y="106.5" font-size="14" text-anchor="middle">VISIT</text>
      <path class="stroke-blue" d="M72 98 q3 11 16 13 M83 106 l5 5 -6 3"/>
      <g transform="translate(14 129)">
        <circle class="stroke-navy" r="5"/><ellipse class="stroke-navy" rx="2.2" ry="5"/><line class="stroke-navy" x1="-5" x2="5"/>
      </g>
      <text class="web-address" x="23" y="133" font-size="10.5">www.pellwayjourneys.com.au</text>
    </g>
  </svg>

  <!-- Vertical banner 1 -->
  <svg class="banner banner--tall" style="left:682px; top:134px;" width="120" height="520" viewBox="0 0 150 650">
    <defs>
      <clipPath id="clip-tall-1"><rect width="150" height="650"/></clipPath>
      <linearGradient id="photo-tall-1" x1="0" x2="1" y1="0" y2="1">
        <stop offset="0" stop-color="#e6e2da"/><stop offset=".5" stop-color="#a08868"/><stop offset="1" stop-color="#5d4a3a"/>
      </linearGradient>
    </defs>
    <g clip-path="url(#clip-tall-1)">
      <rect class="fill-white" width="150" height="650"/>
      <rect class="fill-gold" x="10" y="-4" width="14" height="28" transform="rotate(-20 17 10)"/>
      <ellipse class="fill-gold-soft" cx="150" cy="45" rx="8" ry="14"/>
      <rect class="fill-gold" x="76" y="78" width="8" height="8" transform="rotate(40 80 82)"/>
      <rect class="fill-gold" x="112" y="552" width="7" height="12" transform="rotate(15 115 558)"/>
      <g role="img" aria-label="Photo: business traveller walking through an airport terminal with a suitcase">
        <rect y="270" width="150" height="270" fill="url(#photo-tall-1)"/>
      </g>
      <ellipse class="fill-blue" cx="75" cy="598" rx="160" ry="92"/>
      <ellipse class="fill-white" cx="70" cy="612" rx="170" ry="94"/>
      <circle class="fill-blue" cx="82" cy="226" r="132"/>
      <circle class="fill-navy" cx="72" cy="230" r="128"/>
      <text class="brand-name" x="75" y="52" font-size="15.5" text-anchor="middle">Pellway Journeys</text>
      <text class="headline" x="70" y="160" font-size="17" text-anchor="middle">CELEBRATE</text>
      <text class="big-number" x="66" y="246" font-size="88" text-anchor="middle">40</text>
      <g transform="translate(100 205) rotate(12)">
        <polygon class="fill-red" points="-26,-11 28,-11 23,0 28,11 -26,11"/>
        <text class="tag-text" x="0" y="5" font-size="14" text-anchor="middle" transform="skewX(-12)">YEARS</text>
      </g>
      <text class="tagline" x="74" y="270" font-size="13.5" text-anchor="middle">SERVICE THROUGH</text>
      <text class="tagline" x="74" y="286" font-size="13.5" text-anchor="middle">EXPERIENCE SINCE 1983</text>
      <rect class="fill-blue" x="45" y="560" width="60" height="22" rx="11"/>
      <text class="visit-text" x="75" y="576.5" font-size="14" text-anchor="middle">VISIT</text>
      <path class="stroke-blue" d="M103 586 q0 14 12 20 M108 606 l7 0 -1 -7"/>
      <g transform="translate(76 607)">
        <circle class="stroke-navy" r="5"/><ellipse class="stroke-navy" rx="2.2" ry="5"/><line class="stroke-navy" x1="-5" x2="5"/>
      </g>
      <text class="web-address web-address--condensed" x="75" y="631" font-size="11.5" text-anchor="middle">www.pellwayjourneys.com.au</text>
    </g>
  </svg>

  <!-- Vertical banner 2 -->
  <svg class="banner banner--tall" style="left:856px; top:134px;" width="120" height="520" viewBox="0 0 150 650">
    <defs>
      <clipPath id="clip-tall-2"><rect width="150" height="650"/></clipPath>
      <linearGradient id="photo-tall-2" x1="0" x2="1" y1="0" y2="1">
        <stop offset="0" stop-color="#dde6e8"/><stop offset=".55" stop-color="#8fa3a2"/><stop offset="1" stop-color="#4e5a5a"/>
      </linearGradient>
    </defs>
    <g clip-path="url(#clip-tall-2)">
      <rect class="fill-white" width="150" height="650"/>
      <rect class="fill-gold" x="10" y="-4" width="14" height="28" transform="rotate(-20 17 10)"/>
      <ellipse class="fill-gold-soft" cx="150" cy="45" rx="8" ry="14"/>
      <rect class="fill-gold" x="76" y="78" width="8" height="8" transform="rotate(40 80 82)"/>
      <rect class="fill-gold" x="112" y="552" width="7" height="12" transform="rotate(15 115 558)"/>
      <g role="img" aria-label="Photo: smiling woman in a grey coat checking her phone in an airport with a handbag">
        <rect y="270" width="150" height="270" fill="url(#photo-tall-2)"/>
      </g>
      <ellipse class="fill-blue" cx="75" cy="598" rx="160" ry="92"/>
      <ellipse class="fill-white" cx="70" cy="612" rx="170" ry="94"/>
      <circle class="fill-blue" cx="82" cy="226" r="132"/>
      <circle class="fill-navy" cx="72" cy="230" r="128"/>
      <text class="brand-name" x="75" y="52" font-size="15.5" text-anchor="middle">Pellway Journeys</text>
      <text class="headline" x="70" y="160" font-size="17" text-anchor="middle">CELEBRATE</text>
      <text class="big-number" x="66" y="246" font-size="88" text-anchor="middle">40</text>
      <g transform="translate(100 205) rotate(12)">
        <polygon class="fill-red" points="-26,-11 28,-11 23,0 28,11 -26,11"/>
        <text class="tag-text" x="0" y="5" font-size="14" text-anchor="middle" transform="skewX(-12)">YEARS</text>
      </g>
      <text class="tagline tagline--light" x="74" y="270" font-size="13.5" text-anchor="middle">SERVICE THROUGH</text>
      <text class="tagline tagline--light" x="74" y="286" font-size="13.5" text-anchor="middle">EXPERIENCE SINCE <tspan class="tagline-year">1983</tspan></text>
      <rect class="fill-blue" x="45" y="560" width="60" height="22" rx="11"/>
      <text class="visit-text" x="75" y="576.5" font-size="14" text-anchor="middle">VISIT</text>
      <path class="stroke-blue" d="M103 586 q0 14 12 20 M108 606 l7 0 -1 -7"/>
      <g transform="translate(76 607)">
        <circle class="stroke-navy" r="5"/><ellipse class="stroke-navy" rx="2.2" ry="5"/><line class="stroke-navy" x1="-5" x2="5"/>
      </g>
      <text class="web-address web-address--condensed" x="75" y="631" font-size="11.5" text-anchor="middle">www.pellwayjourneys.com.au</text>
    </g>
  </svg>

  <!-- Vertical banner 3 -->
  <svg class="banner banner--tall" style="left:1027px; top:134px;" width="120" height="520" viewBox="0 0 150 650">
    <defs>
      <clipPath id="clip-tall-3"><rect width="150" height="650"/></clipPath>
      <linearGradient id="photo-tall-3" x1="0" x2="1" y1="0" y2="1">
        <stop offset="0" stop-color="#f2f3f5"/><stop offset=".5" stop-color="#c9b79c"/><stop offset="1" stop-color="#6f8aa6"/>
      </linearGradient>
    </defs>
    <g clip-path="url(#clip-tall-3)">
      <rect class="fill-white" width="150" height="650"/>
      <rect class="fill-gold" x="10" y="-4" width="14" height="28" transform="rotate(-20 17 10)"/>
      <ellipse class="fill-gold-soft" cx="150" cy="45" rx="8" ry="14"/>
      <rect class="fill-gold" x="76" y="78" width="8" height="8" transform="rotate(40 80 82)"/>
      <rect class="fill-gold" x="112" y="552" width="7" height="12" transform="rotate(15 115 558)"/>
      <g role="img" aria-label="Photo: cheerful colleagues working together at a laptop in a bright office">
        <rect y="270" width="150" height="270" fill="url(#photo-tall-3)"/>
      </g>
      <ellipse class="fill-blue" cx="75" cy="598" rx="160" ry="92"/>
      <ellipse class="fill-white" cx="70" cy="612" rx="170" ry="94"/>
      <circle class="fill-blue" cx="82" cy="226" r="132"/>
      <circle class="fill-navy" cx="72" cy="230" r="128"/>
      <text class="brand-name" x="75" y="52" font-size="15.5" text-anchor="middle">Pellway Journeys</text>
      <text class="headline" x="70" y="160" font-size="17" text-anchor="middle">CELEBRATE</text>
      <text class="big-number" x="66" y="246" font-size="88" text-anchor="middle">40</text>
      <g transform="translate(100 205) rotate(12)">
        <polygon class="fill-red" points="-26,-11 28,-11 23,0 28,11 -26,11"/>
        <text class="tag-text" x="0" y="5" font-size="14" text-anchor="middle" transform="skewX(-12)">YEARS</text>
      </g>
      <text class="tagline tagline--light" x="74" y="270" font-size="13.5" text-anchor="middle">SERVICE THROUGH</text>
      <text class="tagline tagline--light" x="74" y="286" font-size="13.5" text-anchor="middle">EXPERIENCE SINCE <tspan class="tagline-year">1983</tspan></text>
      <rect class="fill-blue" x="45" y="560" width="60" height="22" rx="11"/>
      <text class="visit-text" x="75" y="576.5" font-size="14" text-anchor="middle">VISIT</text>
      <path class="stroke-blue" d="M103 586 q0 14 12 20 M108 606 l7 0 -1 -7"/>
      <g transform="translate(76 607)">
        <circle class="stroke-navy" r="5"/><ellipse class="stroke-navy" rx="2.2" ry="5"/><line class="stroke-navy" x1="-5" x2="5"/>
      </g>
      <text class="web-address web-address--condensed" x="75" y="631" font-size="11.5" text-anchor="middle">www.pellwayjourneys.com.au</text>
    </g>
  </svg>
</body>
</html>
```